Vormex Business Card

We are a security company in Central Aus, we supply guards, patrols, alarm monitoring, cash in transit, major event security.

I would like a modern card, possibly matte finish with gloss logo.... up for anything really

Our business colors are black white and blue.

on the back side of the card i was thinking having our logo just centered or our slogan ( "Securing Your Territory 24/7" )

Industry/Entity Type

Security

Contact Information for Business Card

Company Name: Vormex Security Service
My Name: Gareth Pelling
Position: Director
Mobil: 0452 918 307
Work: 89 612 734
Fax: 89 61 48 23
Email: gary.pelling@vormex.com.au
web: vormex.com.au
Address: 14 Brindle Road Alice Springs NT 0870

```html
<!DOCTYPE html>
<html lang="en">
<head>
<meta charset="utf-8">
<title>Vormex Business Card</title>
<link rel="stylesheet" href="https://fonts.googleapis.com/css2?family=Open+Sans:wght@300;400;700&display=swap">
<style>
  :root {
    --stage: #c9cdd3;
    --card-light: #ffffff;
    --card-shade: #e2e3e5;
    --brand-blue: #0b84cc;
    --swoosh-grey: #a7a9ac;
    --swoosh-pale: #d3d4d6;
    --name-grey: #9a9a9a;
    --title-grey: #a8a8a8;
    --on-blue: #ffffff;
  }
  * { margin: 0; padding: 0; box-sizing: border-box; }
  html, body {
    width: 1200px; height: 866px; overflow: hidden;
    background: var(--stage);
    font-family: "Open Sans", Arial, sans-serif;
  }
  .stage { position: relative; width: 1200px; height: 866px; }
  .card {
    position: absolute; width: 520px; height: 310px; overflow: hidden;
    background: linear-gradient(135deg, var(--card-light) 0%, #f2f2f3 55%, var(--card-shade) 100%);
    box-shadow: 0 6px 18px rgba(0,0,0,.18);
  }
  .card--back { left: 70px; top: 150px; }
  .card--front { left: 610px; top: 410px; }

  .wordmark {
    color: var(--brand-blue); font-weight: 700; letter-spacing: 1px; line-height: 1;
  }
  .card--back .wordmark {
    position: absolute; left: 0; right: 0; top: 50%; transform: translateY(-50%);
    text-align: center; font-size: 64px;
  }
  .card--front .wordmark {
    position: absolute; left: 40px; top: 48px; font-size: 46px;
  }

  .card__waves { position: absolute; inset: 0; width: 520px; height: 310px; }

  .holder { position: absolute; left: 42px; top: 196px; }
  .holder__name { font-size: 15px; font-weight: 700; color: var(--name-grey); }
  .holder__title { font-size: 15px; font-weight: 300; color: var(--title-grey); margin-top: 2px; }

  .contact {
    position: absolute; right: 22px; top: 86px; list-style: none;
    text-align: right; color: var(--on-blue); font-size: 11.5px; line-height: 17px;
  }
  .contact li { display: flex; justify-content: flex-end; align-items: center; gap: 5px; }
  .contact svg { width: 10px; height: 10px; fill: var(--on-blue); }
</style>
</head>
<body>
<main class="stage">
  <section class="card card--back" aria-label="Card back">
    <div class="wordmark">Vormex</div>
  </section>

  <section class="card card--front" aria-label="Card front">
    <svg class="card__waves" viewBox="0 0 520 310" aria-hidden="true">
      <path d="M372 0 C318 150 262 262 0 262 L0 310 L520 310 L520 0 Z" fill="var(--swoosh-pale)"/>
      <path d="M360 40 C330 160 250 250 40 262 C270 238 338 170 376 40 Z" fill="var(--swoosh-grey)"/>
      <path d="M392 0 C346 170 280 278 0 284 L0 310 L520 310 L520 0 Z" fill="var(--swoosh-grey)"/>
      <path d="M404 0 C360 180 292 290 0 296 L0 310 L520 310 L520 0 Z" fill="var(--brand-blue)"/>
    </svg>

    <div class="wordmark">Vormex</div>

    <div class="holder">
      <div class="holder__name">Maren Coulby-Hale</div>
      <div class="holder__title">Consultant</div>
    </div>

    <ul class="contact">
      <li>27 Kestrel Lane,Unit 4</li>
      <li>Harbour Park QLN</li>
      <li>013 482 7265
        <svg viewBox="0 0 10 10" aria-hidden="true"><path d="M2 0.5 L3.6 2.6 L2.7 3.6 C3.3 5 4.9 6.6 6.4 7.3 L7.4 6.4 L9.5 8 L8.4 9.5 C4.8 9.3 0.7 5.2 0.5 1.6 Z"/></svg>
      </li>
      <li>013 482 7265
        <svg viewBox="0 0 10 10" aria-hidden="true"><rect x="2.5" y="0.5" width="5" height="3"/><rect x="0.5" y="4" width="9" height="5"/></svg>
      </li>
      <li>hello@mailbox.com
        <svg viewBox="0 0 10 10" aria-hidden="true"><path d="M0.5 2 H9.5 V8.5 H0.5 Z M0.5 2 L5 5.5 L9.5 2" stroke="var(--brand-blue)" stroke-width="0.8"/></svg>
      </li>
      <li>www.sitenameplace.com</li>
    </ul>
  </section>
</main>
</body>
</html>
```